Please look at my website to get a better understanding of my business: www.perovatu.com
This business is about Life Coaching for Families, couples, teenagers and individuals. I work more w parents of teenagers (as well as teenagers) but not so much with young kids.
The card should be fun, not too busy, with a sense of flow and playfulness. Warm colors, artistic style (can have a family sculpture, paining or a picture in it). Basic information about myself and my company

Reason: I extended my due date for next Tuesday, November 13th. Please summit new designs if you haven't done so, and for those who submitted, thank you so much for your time and effort. I will make a decision next Tues, and will contact you if I need to revise some items. Much thanks to you all! Orla

Families, parents, teenagers, couples, individuals.

Business

• Business name: PeRoVaTu! Hearth Circle Life Coaching
My name: Orla Bekwith, RMTQ
Description of my work: Tri-Mode life coach
Tel: 555-304-7719
Website: www.perovatu.com
• Family sculpture, abstract painting or a picture, or simply a nice background w/out a picture added.
• Corporate feeling, cold colors, corporate symbols. no Sunset, or picture of families on the beach.
Don't include bar-code (from uploaded file 1, it is only the designer to find out more about my website).

```html
<!DOCTYPE html>
<html lang="en">
<head>
<meta charset="utf-8">
<title>Perovatu Business Card</title>
<link href="https://fonts.googleapis.com/css2?family=Source+Sans+3:wght@400;600&display=swap" rel="stylesheet">
<style>
  :root {
    --backdrop: #000000;
    --card: #ffffff;
    --orange-deep: #e97e12;
    --orange-mid: #f29433;
    --orange-light: #f6ad5c;
    --ink: #1a1a1a;
    --brand-ink: #3a3a3c;
    --tagline-ink: #4a4a4c;
    --accent-blue: #0c8ac9;
  }
  * { margin: 0; padding: 0; box-sizing: border-box; }
  html, body {
    width: 1200px;
    height: 1000px;
    overflow: hidden;
    background: var(--backdrop);
  }
  .canvas {
    position: relative;
    width: 1200px;
    height: 1000px;
    background: var(--backdrop);
    font-family: "Source Sans 3", "Myriad Pro", sans-serif;
  }
  .business-card {
    position: absolute;
    left: 62px;
    top: 166px;
    width: 1091px;
    height: 637px;
    background: var(--card);
    overflow: hidden;
  }
  .art-panel {
    position: absolute;
    left: 0;
    top: 0;
    width: 386px;
    height: 637px;
    background:
      radial-gradient(ellipse at 30% 45%, var(--orange-light) 0%, rgba(246,173,92,0) 55%),
      radial-gradient(ellipse at 75% 75%, var(--orange-light) 0%, rgba(246,173,92,0) 50%),
      linear-gradient(160deg, var(--orange-deep) 0%, var(--orange-mid) 55%, var(--orange-deep) 100%);
    box-shadow: 6px 0 10px rgba(0,0,0,0.28);
    z-index: 1;
  }
  .brand {
    position: absolute;
    left: 518px;
    top: 112px;
    width: 462px;
  }
  .brand-name {
    display: flex;
    align-items: center;
    justify-content: flex-end;
    gap: 16px;
    font-size: 92px;
    font-weight: 400;
    line-height: 1;
    color: var(--brand-ink);
  }
  .brand-dot {
    width: 22px;
    height: 22px;
    border-radius: 50%;
    background: var(--accent-blue);
    flex-shrink: 0;
  }
  .brand-tagline {
    margin-top: 8px;
    text-align: right;
    font-size: 18px;
    font-weight: 600;
    color: var(--tagline-ink);
  }
  .coach {
    position: absolute;
    left: 568px;
    top: 298px;
    width: 352px;
    text-align: center;
    font-size: 27px;
    line-height: 38px;
    color: var(--ink);
  }
  .contact {
    position: absolute;
    left: 428px;
    top: 478px;
    font-size: 27px;
    line-height: 46px;
    color: var(--ink);
  }
</style>
</head>
<body>
  <main class="canvas">
    <section class="business-card">
      <div class="art-panel" role="img" aria-label="Abstract warm orange painting of a family sculpture with flowing swirls"></div>

      <header class="brand">
        <div class="brand-name"><span class="brand-dot"></span><span>Perovatu</span></div>
        <p class="brand-tagline">Hearth Circle Life Coaching</p>
      </header>

      <div class="coach">
        <p class="coach-name">Orla Bekwith, RMTQ</p>
        <p class="coach-role">Tri-Mode life coach</p>
      </div>

      <div class="contact">
        <p class="contact-phone">Tel: 555-304-7719</p>
        <p class="contact-web">Website: www.perovatu.com</p>
      </div>
    </section>
  </main>
</body>
</html>
```